Business Card Design Project

Keep it simple , using logo and colors that compliment. Logo on one side with complimentary back ground color. Other side, personal info with possible complimentary design/colors

Target Market(s)

we are a non for profit that will be seeking donations . Both monetary and in kind

Industry/Entity Type

Business

Font styles to use
Sans Serif

Colors

Designer to choose colors to be used in the design.

```html
<!DOCTYPE html>
<html lang="en">
<head>
<meta charset="utf-8">
<title>Open Hands Trust – Business Card</title>
<link rel="stylesheet" href="https://fonts.googleapis.com/css2?family=Open+Sans:wght@400;600;700&display=swap">
<style>
  :root {
    --navy: #272c4c;
    --yellow: #e8c800;
    --paper: #f4f4f2;
    --card-white: #ffffff;
    --backdrop: #e6e7e8;
    --ink: #2a2d3e;
    --ink-soft: #4a4d5c;
  }
  * { box-sizing: border-box; margin: 0; padding: 0; }
  html, body {
    width: 1200px; height: 675px; overflow: hidden;
    background: var(--backdrop);
    font-family: "Open Sans", Arial, sans-serif;
    color: var(--ink);
  }
  .canvas {
    position: relative; width: 1200px; height: 675px;
    display: flex; align-items: center; justify-content: center; gap: 60px;
  }
  .card {
    position: relative; width: 520px; height: 297px; overflow: hidden;
    box-shadow: 0 6px 18px rgba(0,0,0,0.12);
  }
  /* Front side */
  .card-front {
    background: var(--card-white);
    display: flex; align-items: center; justify-content: center; gap: 16px;
  }
  .brand-dot {
    width: 34px; height: 34px; border-radius: 50%;
    background: var(--navy); flex: none;
  }
  .brand-name {
    font-weight: 600; font-size: 34px; color: var(--navy);
    letter-spacing: 0.5px; white-space: nowrap;
  }
  /* Back side */
  .card-back { background: var(--paper); }
  .card-back .brand {
    position: absolute; left: 36px; top: 130px;
    display: flex; align-items: center; gap: 10px;
  }
  .card-back .brand-dot { width: 22px; height: 22px; }
  .card-back .brand-name { font-size: 20px; }
  .holder {
    position: absolute; left: 236px; top: 62px; white-space: nowrap;
  }
  .holder-name { font-weight: 700; font-size: 17px; color: var(--navy); line-height: 1.2; }
  .holder-role { font-size: 10px; color: var(--ink-soft); margin-top: 2px; }
  .divider {
    position: absolute; left: 292px; right: 16px; top: 118px;
    height: 1px; background: var(--yellow);
  }
  .contacts {
    position: absolute; left: 292px; top: 128px; list-style: none;
    font-size: 11px; color: var(--ink); line-height: 1.6; white-space: nowrap;
  }
  .contacts li { display: flex; align-items: center; gap: 7px; }
  .contacts svg { width: 10px; height: 10px; fill: var(--navy); flex: none; }
  .contacts .pair { display: inline-flex; align-items: center; gap: 6px; margin-left: 6px; }
  .bands { position: absolute; left: 0; bottom: 0; width: 520px; height: 60px; }
</style>
</head>
<body>
<main class="canvas">
  <section class="card card-front" aria-label="Card front">
    <span class="brand-dot"></span>
    <span class="brand-name">Open Hands Trust</span>
  </section>

  <section class="card card-back" aria-label="Card back">
    <div class="brand">
      <span class="brand-dot"></span>
      <span class="brand-name">Open Hands Trust</span>
    </div>

    <div class="holder">
      <p class="holder-name">Your Long Name</p>
      <p class="holder-role">Owner / President</p>
    </div>
    <div class="divider"></div>

    <ul class="contacts">
      <li>
        <svg viewBox="0 0 12 12"><path d="M6 0a4 4 0 0 0-4 4c0 3 4 8 4 8s4-5 4-8a4 4 0 0 0-4-4zm0 5.6A1.6 1.6 0 1 1 6 2.4a1.6 1.6 0 0 1 0 3.2z"/></svg>
        Your Commercial or office address
      </li>
      <li>
        <svg viewBox="0 0 12 12"><path d="M1 3c2-2 8-2 10 0l-1 2-2-1V3H4v1L2 5zM2 7h8v4H2z"/></svg>
        00.00.00.0000
        <span class="pair">
          <svg viewBox="0 0 12 12"><path d="M3 0h6v3H3zM1 4h10v5H9v3H3V9H1zm3 5v2h4V9z"/></svg>
          00.00.00.0000
        </span>
      </li>
      <li>
        <svg viewBox="0 0 12 12"><path d="M0 2h12v8H0zm1 1v.4l5 3.2 5-3.2V3zm0 1.6V9h10V4.6L6 7.8z"/></svg>
        yourname@yourwebsite.com
      </li>
      <li>
        <svg viewBox="0 0 12 12"><circle cx="6" cy="6" r="5.5"/><path d="M0.5 6h11M6 .5c-3 3-3 8 0 11M6 .5c3 3 3 8 0 11" stroke="#f4f4f2" stroke-width="0.9" fill="none"/></svg>
        www.yourwebsite.com
      </li>
    </ul>

    <svg class="bands" viewBox="0 0 520 60" preserveAspectRatio="none" aria-hidden="true">
      <polygon points="375,40 388,33 520,33 520,40" fill="var(--yellow)"/>
      <polygon points="0,51 350,51 375,40 520,40 520,60 0,60" fill="var(--navy)"/>
    </svg>
  </section>
</main>
</body>
</html>
```